Business Card/Email Signature design

We need an new business card design for our business as well as an animated email signature design.<br/>Business Card:<br/>The business card designs need to have the following information for each director:<br/>Leon Bramwell<br/>Managing Director<br/>leon@talvoraworks.com.au<br/>0498617340<br/>www.talvoraworks.com.au<br/><br/>and<br/><br/>Priscilla Venton<br/>Director<br/>priscilla@talvoraworks.com.au<br/>0467302958<br/>www.talvoraworks.com.au<br/><br/>I will upload the Talvora. Works logo designs to be used for the design. Our colours are black and white. I would like to see the designs in both coloured backgrounds.<br/><br/>For the email signature we need the same information. I also need to add a logo of our association BLPX of which i will add the logo as well. This BLPX logo does not need to be used for the business card unless it works with the design.<br/>For the animation part of the logo our company is called Talvora. Works - We have a number of divisions called Talvora. Construct, Talvora. Property, Talvora. Sales, Talvora. Executive Support, Talvora. Private PA, Talvora. Talent and Talvora. Coaching<br/>I would like for the email Signature to be designed so that the Talvora. stays still but the words Construct, Property, Sales, Executive Support, Private PA, Talent and Coaching rotate through to capture attention and tell the story of what we do.<br/><br/>Any questions please don't hesitate to message me.

Industry/Entity Type

Recruiter

Contact Information for Business Card

Leon Bramwell
Managing Director
leon@talvoraworks.com.au
0498617340
www.talvoraworks.com.au

Priscilla Venton
Director
priscilla@talvoraworks.com.au
0467302958
www.talvoraworks.com.au

Font styles to use
Serif

Colors

Designer to choose colors to be used in the design.

Requirements
Must have
• The animation for the email signature as described
Should not have
• Any changes to my logo. Any colour other that black or white

```html
<!DOCTYPE html>
<html lang="en">
<head>
<meta charset="utf-8">
<title>Talvora. Works — Business Card</title>
<link rel="stylesheet" href="https://fonts.googleapis.com/css2?family=Libre+Caslon+Text:wght@400&family=Work+Sans:wght@400;500&display=swap">
<style>
  :root {
    --backdrop: #b9b9b9;
    --card-dark: #1f1d1e;
    --card-light: #ffffff;
    --ink-light: #ffffff;
    --ink-dark: #1b1b1b;
    --ink-muted: #3a3a3a;
  }
  * { margin: 0; padding: 0; box-sizing: border-box; }
  html, body {
    width: 1200px;
    height: 930px;
    overflow: hidden;
    background: var(--backdrop);
  }
  .canvas {
    position: relative;
    width: 1200px;
    height: 930px;
  }
  .card {
    position: absolute;
    width: 620px;
    height: 354px;
    border-radius: 22px;
    box-shadow: 0 6px 18px rgba(0,0,0,0.25);
  }
  .card--front {
    left: 120px;
    top: 70px;
    background: var(--card-dark);
    display: flex;
    align-items: center;
    justify-content: center;
  }
  .card--back {
    left: 460px;
    top: 506px;
    background: var(--card-light);
  }
  .brand {
    display: flex;
    align-items: center;
    gap: 14px;
    font-family: "Libre Caslon Text", serif;
    font-weight: 400;
    text-transform: uppercase;
    letter-spacing: 0.06em;
  }
  .brand__mark {
    width: 22px;
    height: 22px;
    border: 1.5px solid currentColor;
  }
  .card--front .brand {
    color: var(--ink-light);
    font-size: 30px;
  }
  .card--back .brand {
    position: absolute;
    left: 42px;
    top: 58px;
    color: var(--ink-dark);
    font-size: 22px;
  }
  .contact {
    position: absolute;
    left: 330px;
    top: 170px;
    font-family: "Work Sans", sans-serif;
    color: var(--ink-dark);
  }
  .contact__name {
    font-size: 27px;
    font-weight: 500;
    letter-spacing: 0.04em;
    text-transform: uppercase;
    line-height: 1.1;
  }
  .contact__role {
    font-size: 15px;
    color: var(--ink-muted);
    margin: 4px 0 16px 22px;
  }
  .contact__list {
    list-style: none;
    font-size: 15px;
    line-height: 1.55;
    margin-left: 22px;
  }
  .contact__list li {
    display: flex;
    align-items: center;
    gap: 7px;
  }
  .contact__list svg {
    width: 11px;
    height: 11px;
    flex: none;
  }
</style>
</head>
<body>
<main class="canvas">
  <section class="card card--front" aria-label="Card front">
    <div class="brand"><span class="brand__mark"></span><span>Talvora. Works</span></div>
  </section>

  <section class="card card--back" aria-label="Card back">
    <div class="brand"><span class="brand__mark"></span><span>Talvora. Works</span></div>
    <div class="contact">
      <h1 class="contact__name">Leon Bramwell</h1>
      <p class="contact__role">Managing Director</p>
      <ul class="contact__list">
        <li>
          <svg viewBox="0 0 12 12" aria-hidden="true"><path d="M3 1 L5 3.5 L4 5 Q5 7.5 7 8 L8.5 7 L11 9 L9.5 11 Q2 10 1 2.5 Z" fill="none" stroke="#1b1b1b" stroke-width="1.1" stroke-linejoin="round"/></svg>
          <span>0498617340</span>
        </li>
        <li>
          <svg viewBox="0 0 12 12" aria-hidden="true"><rect x="1" y="2.5" width="10" height="7" fill="none" stroke="#1b1b1b" stroke-width="1.1"/><path d="M1 2.5 L6 6.5 L11 2.5" fill="none" stroke="#1b1b1b" stroke-width="1.1"/></svg>
          <span>leon@talvoraworks.com.au</span>
        </li>
        <li>
          <svg viewBox="0 0 12 12" aria-hidden="true"><circle cx="6" cy="6" r="5" fill="none" stroke="#1b1b1b" stroke-width="1.1"/><ellipse cx="6" cy="6" rx="2.2" ry="5" fill="none" stroke="#1b1b1b" stroke-width="0.9"/><path d="M1 6 H11" stroke="#1b1b1b" stroke-width="0.9"/></svg>
          <span>www.talvoraworks.com.au</span>
        </li>
      </ul>
    </div>
  </section>
</main>
</body>
</html>
```